Business Card Design

I need a business card for my company i am starting. I will be providing stump grinding services. I use a motorized machine to grind stumps down under the ground so that they are out of the way and out of sight. I'm looking for my card to have maroon or dark red somewhere in the card to match my truck. I'm going to use this card to advertise and also serve as a design to wrap my truck tailgate as advertisement so i want it to match. the dark maroon color of my truck. I wouldn't mind using bright colors or color for the rest of the card or the lettering or any designs on the card. In the images i have provided i like how there are saw blades integrated into these people advertisements. I also like the illustration of the stump grinder. I also provided a picture of the actual cutting wheel or blade of the grinder.

Industry/Entity Type

Business

Contact Information for Business Card

Company Name - Oakline Stump Grinding
Phone - 407-219-5573
Email - harlow.stumpwork@quillpost.net
Name and title - Thomas Harlow - Owner and operator
Company Slogan - You point them out, I'll clear them

```html
<!DOCTYPE html>
<html lang="en">
<head>
<meta charset="utf-8">
<title>Oakline Stump Grinding – Business Card</title>
<link rel="stylesheet" href="https://fonts.googleapis.com/css2?family=Ubuntu:wght@400;500;700&display=swap">
<style>
  :root {
    --page-bg: #ece7df;
    --card-red: #b11e26;
    --card-red-deep: #8f151c;
    --photo-dark: #5a4630;
    --photo-mid: #a88a5e;
    --photo-light: #d9c79a;
    --ink-light: #ffffff;
  }
  * { box-sizing: border-box; margin: 0; padding: 0; }
  html, body {
    width: 1200px;
    height: 780px;
    overflow: hidden;
    background: var(--page-bg);
    font-family: "Ubuntu", sans-serif;
  }
  .canvas {
    width: 1200px;
    height: 780px;
    display: flex;
    align-items: center;
    justify-content: center;
  }
  .business-card {
    width: 1050px;
    height: 600px;
    display: flex;
    overflow: hidden;
    box-shadow: 0 14px 40px rgba(0,0,0,0.22);
  }
  .grinder-photo {
    width: 380px;
    height: 100%;
    flex-shrink: 0;
    background:
      radial-gradient(circle at 62% 55%, var(--photo-light) 0%, var(--photo-mid) 38%, transparent 60%),
      linear-gradient(160deg, var(--photo-dark) 0%, var(--photo-mid) 55%, var(--photo-light) 100%);
  }
  .card-info {
    flex: 1;
    background: linear-gradient(135deg, var(--card-red) 0%, var(--card-red-deep) 100%);
    color: var(--ink-light);
    padding: 90px 36px 0 56px;
  }
  .brand {
    display: flex;
    align-items: center;
    gap: 18px;
  }
  .brand-dot {
    width: 34px;
    height: 34px;
    border-radius: 50%;
    background: var(--ink-light);
    flex-shrink: 0;
  }
  .brand-name {
    font-size: 36px;
    font-weight: 700;
    line-height: 1.1;
    white-space: nowrap;
  }
  .slogan {
    margin: 10px 0 0 52px;
    font-size: 22px;
    font-weight: 400;
    white-space: nowrap;
  }
  .person {
    margin: 60px 0 0 52px;
  }
  .person-name {
    font-size: 36px;
    font-weight: 700;
    line-height: 1.15;
  }
  .person-title {
    font-size: 22px;
    font-weight: 500;
    margin-top: 4px;
  }
  .contact {
    margin: 48px 0 0 52px;
    font-size: 22px;
    font-weight: 500;
    line-height: 1.9;
    white-space: nowrap;
  }
</style>
</head>
<body>
  <main class="canvas">
    <article class="business-card">
      <div class="grinder-photo" role="img" aria-label="Close-up photo of a stump grinder cutting wheel churning through soil and wood chips"></div>
      <section class="card-info">
        <div class="brand">
          <span class="brand-dot"></span>
          <h1 class="brand-name">Oakline Stump Grinding</h1>
        </div>
        <p class="slogan">You point them out, I'll clear them</p>
        <div class="person">
          <p class="person-name">Thomas Harlow</p>
          <p class="person-title">Owner and operator</p>
        </div>
        <div class="contact">
          <p class="contact-phone">407-219-5573</p>
          <p class="contact-email">harlow.stumpwork@quillpost.net</p>
        </div>
      </section>
    </article>
  </main>
</body>
</html>
```